Business Card Design Project

2 sided business card utilizing existing logo
- English on one side, Arabic on the other side (both English and Arabic text will be provided)
Same color scheme as logo
Information included will be: name, title, email, phone, address and website (www.dravelnix.com)
Updates

Target Market(s)

We are a Systems Integration Company

Industry/Entity Type

Business

Font styles to use
Serif
Sans Serif

Requirements
Should not have
• We prefer using the flat logo rather than one with shadow/3D effect

```html
<!DOCTYPE html>
<html lang="en">
<head>
<meta charset="utf-8">
<title>Business Card – Front and Back</title>
<link rel="stylesheet" href="https://fonts.googleapis.com/css2?family=Roboto:wght@400;700&family=Roboto+Condensed:wght@500;700&display=swap">
<style>
  :root {
    --backdrop: #e9e6e1;
    --card: #ffffff;
    --teal: #418d98;
    --sky: #6dbaea;
    --ring: #7d8288;
    --ink: #1f2326;
    --ink-soft: #3a3f44;
  }
  * { box-sizing: border-box; margin: 0; padding: 0; }
  html, body { width: 1200px; height: 913px; overflow: hidden; }
  body {
    background: var(--backdrop);
    font-family: "Roboto", Arial, sans-serif;
    position: relative;
  }
  .card {
    position: absolute;
    top: 302px;
    width: 540px;
    height: 309px;
    background: var(--card);
    box-shadow: 0 6px 18px rgba(0,0,0,.18);
    overflow: hidden;
  }
  .card--front { left: 40px; }
  .card--back { left: 620px; }

  .edge-band {
    position: absolute;
    bottom: 0; left: 0; right: 0;
    height: 22px;
    display: flex;
    gap: 4px;
  }
  .edge-band__teal { background: var(--teal); }
  .edge-band__sky { background: var(--sky); }
  .card--front .edge-band__teal { flex: 0 0 77%; }
  .card--front .edge-band__sky { flex: 1; }
  .card--back .edge-band__sky { flex: 0 0 40%; }
  .card--back .edge-band__teal { flex: 1; }

  .logo-mark {
    position: absolute;
    border: 3px solid var(--ring);
    border-radius: 50%;
    display: flex;
    align-items: center;
    justify-content: center;
  }
  .logo-mark__name {
    font-family: "Roboto Condensed", "Arial Narrow", sans-serif;
    font-weight: 700;
    color: var(--teal);
    line-height: 0.95;
    text-align: center;
  }
  .logo-mark__line { display: block; }
  .card--front .logo-mark { width: 170px; height: 170px; left: 185px; top: 50px; }
  .card--front .logo-mark__name { font-size: 38px; }
  .card--back .logo-mark { width: 118px; height: 118px; right: 36px; top: 30px; }
  .card--back .logo-mark__name { font-size: 26px; }

  .holder {
    position: absolute;
    left: 34px;
    top: 96px;
  }
  .holder__name {
    font-family: "Roboto", Arial, sans-serif;
    font-weight: 700;
    font-size: 24px;
    color: var(--teal);
  }
  .holder__title {
    font-size: 12px;
    font-weight: 700;
    color: var(--ink-soft);
    margin-top: 1px;
  }

  .contact-list {
    position: absolute;
    left: 34px;
    top: 168px;
    list-style: none;
    font-family: "Roboto Condensed", "Arial Narrow", sans-serif;
    font-weight: 500;
    font-size: 15px;
    color: var(--ink);
  }
  .contact-list__item {
    display: flex;
    align-items: flex-start;
    gap: 12px;
    margin-bottom: 5px;
    line-height: 1.2;
  }
  .contact-list__icon {
    width: 16px; height: 16px;
    flex: 0 0 16px;
    margin-top: 1px;
    fill: var(--teal);
  }
  .contact-list__icon--ink { fill: var(--ink-soft); }
</style>
</head>
<body>

<section class="card card--front" aria-label="Card front">
  <div class="logo-mark"><span class="logo-mark__name"><span class="logo-mark__line">Your</span><span class="logo-mark__line">Logo</span></span></div>
  <div class="edge-band"><span class="edge-band__teal"></span><span class="edge-band__sky"></span></div>
</section>

<section class="card card--back" aria-label="Card back">
  <div class="logo-mark"><span class="logo-mark__name"><span class="logo-mark__line">Your</span><span class="logo-mark__line">Logo</span></span></div>

  <div class="holder">
    <h1 class="holder__name">Your Name</h1>
    <p class="holder__title">Your Title</p>
  </div>

  <ul class="contact-list">
    <li class="contact-list__item">
      <svg class="contact-list__icon" viewBox="0 0 16 16" aria-hidden="true"><path d="M8 1a5 5 0 0 0-5 5c0 3.6 5 9 5 9s5-5.4 5-9a5 5 0 0 0-5-5zm0 7a2 2 0 1 1 0-4 2 2 0 0 1 0 4z"/></svg>
      <span>Your working address in just<br>two lines</span>
    </li>
    <li class="contact-list__item">
      <svg class="contact-list__icon contact-list__icon--ink" viewBox="0 0 16 16" aria-hidden="true"><path d="M1 5c0-2 3-3 7-3s7 1 7 3v1h-3V5H4v1H1zM4 7h8l2 6H2zm4 1.5a2 2 0 1 0 0 4 2 2 0 0 0 0-4z"/></svg>
      <span>000-000-000-000</span>
    </li>
    <li class="contact-list__item">
      <svg class="contact-list__icon contact-list__icon--ink" viewBox="0 0 16 16" aria-hidden="true"><path d="M1 3h14v10H1zm1.5 1.5L8 9l5.5-4.5z" fill-rule="evenodd"/></svg>
      <span>name@yourwebsite.com</span>
    </li>
    <li class="contact-list__item">
      <svg class="contact-list__icon contact-list__icon--ink" viewBox="0 0 16 16" aria-hidden="true"><circle cx="8" cy="8" r="7"/><path d="M1 8h14M8 1c-3 3-3 11 0 14M8 1c3 3 3 11 0 14M2.5 4.5h11M2.5 11.5h11" stroke="#fff" stroke-width="1" fill="none"/></svg>
      <span>www.yourwebsite.com</span>
    </li>
  </ul>

  <div class="edge-band"><span class="edge-band__sky"></span><span class="edge-band__teal"></span></div>
</section>

</body>
</html>
```